Flyer Design Project

I need an a5 sized flyer designed for my companys Mindfulness Based Stress Reduction course. I would like it to look peaceful but I would like the designer to be a little creative I don't want it to look like every other boring wellness brochure. No cliched images please. The course is about Mindfulness, there is yoga and meditation involved, again don't want your typical yoga and meditation images on it. I want it to look interesting and different.

The attached document has two pages each page should be one side of the leaflet.

Target Market(s)

alternative people who are interested in wellness, stressed out people and people who have health issues and could benefit from Mindfulness

Industry/Entity Type

Wellness

Requirements
Must have
• I want the fact that we are donating to charity to be obvious. But not in a showing off way. I want it known but NOT hey look at how wonderful I am.

Nice to have
• The font similar to my website.

http://www.quietbirchlanewellness.com
Should not have
• Cheesy cliched images of yoga and meditation.

```html
<!DOCTYPE html>
<html lang="en">
<head>
<meta charset="utf-8">
<title>Mindfulness Based Stress Reduction</title>
<link href="https://fonts.googleapis.com/css2?family=Cinzel:wght@400;500&family=Source+Sans+3:wght@500;600;700&family=Crimson+Pro:wght@400;500&display=swap" rel="stylesheet">
<style>
  :root {
    --teal-band: #2d86a3;
    --teal-text: #2a7d9b;
    --plum: #a93c6a;
    --plum-edge: #c8819c;
    --sun: #f2d33a;
    --ink: #1e1e1e;
    --paper: #ffffff;
  }
  html, body { margin: 0; padding: 0; overflow: hidden; background: var(--paper); }
  .flyer {
    position: relative;
    width: 847px;
    height: 1200px;
    overflow: hidden;
    background: var(--paper);
    font-family: "Crimson Pro", "Times New Roman", serif;
    color: var(--ink);
  }
  .hero {
    position: absolute; left: 0; top: 0;
    width: 847px; height: 386px;
    background: var(--teal-band);
  }
  .hero-photo {
    position: absolute; left: 292px; top: 0;
    width: 108px; height: 386px;
    background: linear-gradient(180deg, #b98452 0%, #d8c6b2 38%, #e9e5e0 70%, #d9d6d1 100%);
  }
  .course-tag {
    position: absolute; left: 0; top: 0;
    width: 496px; height: 136px;
    background: var(--plum);
    border-right: 5px solid var(--plum-edge);
    border-bottom: 5px solid var(--plum-edge);
    box-sizing: border-box;
    display: flex; align-items: center; justify-content: center;
    padding-bottom: 22px;
  }
  .course-tag span {
    font-family: "Source Sans 3", Arial, sans-serif;
    font-weight: 600;
    font-size: 39px;
    color: var(--paper);
    letter-spacing: 0.2px;
  }
  .title-word {
    position: absolute;
    top: 158px;
    font-family: "Cinzel", "Trajan Pro", serif;
    font-weight: 400;
    font-size: 62px;
    color: var(--paper);
    line-height: 1;
    letter-spacing: 1px;
  }
  .title-word .initial { font-size: 82px; }
  .title-stress { left: 78px; }
  .title-reduction { left: 410px; }
  .sun-stripe {
    position: absolute; left: 0; top: 386px;
    width: 847px; height: 26px;
    background: var(--sun);
  }
  .content-frame {
    position: absolute; left: 34px; top: 412px;
    width: 780px; height: 760px;
    border: 2px solid var(--sun);
    border-top: none;
    box-sizing: border-box;
  }
  .content {
    position: absolute; left: 72px; top: 466px; width: 728px;
  }
  h1, h2 {
    font-family: "Source Sans 3", Arial, sans-serif;
    color: var(--teal-text);
    margin: 0;
  }
  h1 { font-size: 40px; font-weight: 600; line-height: 1.1; margin-bottom: 8px; }
  h2 { font-size: 28px; font-weight: 600; line-height: 1.2; margin: 20px 0 6px; }
  p { margin: 0; font-size: 19.5px; line-height: 1.22; }
  .lead-in { margin-top: 18px; }
  .outcomes { list-style: none; margin: 14px 0 0; padding: 0; }
  .outcomes li {
    position: relative;
    padding-left: 24px;
    font-size: 19.5px;
    line-height: 1.22;
    margin-bottom: 15px;
  }
  .outcomes li svg { position: absolute; left: 0; top: 5px; }
  .closing { margin-top: 26px; }
</style>
</head>
<body>
<div class="flyer">
  <header class="hero">
    <div class="hero-photo" role="img" aria-label="Photo of a calm dog sitting upright with eyes closed and paws raised in a meditation pose"></div>
    <div class="course-tag"><span>Mindfulness Based</span></div>
    <div class="title-word title-stress"><span class="initial">S</span>TRESS</div>
    <div class="title-word title-reduction"><span class="initial">R</span>EDUCTION</div>
  </header>
  <div class="sun-stripe"></div>
  <div class="content-frame"></div>

  <main class="content">
    <h1>What is Mindfulness?</h1>
    <p>Put simply, mindfulness is about being aware of the present moment, without being caught up in ruminating thoughts or worrying about the past or the future. Mindlessness can result in loss of awareness and in you becoming disconnected from your life. Mindfulness gives us the ability to live more fully as it allows the body and mind to become calmer and more aware.</p>

    <h2>What is Mindfulness Based Stress Reduction (MBSR)?</h2>
    <p>MBSR uses mindful mediation and mindful movement as its basis. The practises have shown over two decades to be transforming in the lives of countless course attendees.</p>

    <p class="lead-in">Published reports point out that the majority of course attendees who complete the 8 weeks:</p>
    <ul class="outcomes">
      <li><svg width="11" height="15" viewBox="0 0 11 15"><path d="M2 1.5 L8.5 7.5 L2 13.5" fill="none" stroke="#2a7d9b" stroke-width="2.6"/></svg>Are more aware</li>
      <li><svg width="11" height="15" viewBox="0 0 11 15"><path d="M2 1.5 L8.5 7.5 L2 13.5" fill="none" stroke="#2a7d9b" stroke-width="2.6"/></svg>Have decreased physical and psychological symptoms</li>
      <li><svg width="11" height="15" viewBox="0 0 11 15"><path d="M2 1.5 L8.5 7.5 L2 13.5" fill="none" stroke="#2a7d9b" stroke-width="2.6"/></svg>Are able to relax and manage stress</li>
      <li><svg width="11" height="15" viewBox="0 0 11 15"><path d="M2 1.5 L8.5 7.5 L2 13.5" fill="none" stroke="#2a7d9b" stroke-width="2.6"/></svg>Have reduced pain levels or an improved ability to cope with pain levels that<br>may or may not go away</li>
      <li><svg width="11" height="15" viewBox="0 0 11 15"><path d="M2 1.5 L8.5 7.5 L2 13.5" fill="none" stroke="#2a7d9b" stroke-width="2.6"/></svg>Live more fully</li>
      <li><svg width="11" height="15" viewBox="0 0 11 15"><path d="M2 1.5 L8.5 7.5 L2 13.5" fill="none" stroke="#2a7d9b" stroke-width="2.6"/></svg>Have improved self esteem and reduced anxiety</li>
      <li><svg width="11" height="15" viewBox="0 0 11 15"><path d="M2 1.5 L8.5 7.5 L2 13.5" fill="none" stroke="#2a7d9b" stroke-width="2.6"/></svg>Are able to cope better in stressful situations</li>
    </ul>

    <p class="closing">Our MBSR courses are closely structured on the approach developed by Dr Elias Marrow and his associates at the Northfield Medical Centre.</p>
  </main>
</div>
</body>
</html>
```